Dynamic Templates

Our company hosts web stores for our clients. They can set up as many as they wish on our platform, and select from the stock templates we provide. We are looking to increase the number of available stock templates.

Because our users can dynamically control many of the template elements - specifically colors - they have to be flexible and abide by certain rules. These rules are spelled out in the attached documents.

Here are links to two of our most used templates:
http://fernridge.vexalcart.example/
http://stampled.vexalcart.example/

Templates need to have a landing page (what you see when first clicking one of the above links). There also needs to be a category page (what you see when clicking any category) and a product detail page (what you see when you arrive at an individual product, where there are various cart options like Buy Now or Request Info).

```html
<!DOCTYPE html>
<html lang="en">
<head>
<meta charset="utf-8">
<title>Leafwell Trio Planter Kit – BrightWares</title>
<link href="https://fonts.googleapis.com/css2?family=Arimo:wght@400;700&family=Roboto+Condensed:wght@400&family=Nunito:wght@400;600&display=swap" rel="stylesheet">
<style>
:root{
  --page:#ffffff;
  --ink:#111111;
  --navy:#1b3f5c;
  --link:#1f6fa6;
  --orange:#f08a1c;
  --grey:#777777;
  --panel:#c6dfea;
  --nav:#c2dde9;
  --nav-dark:#9ec3d4;
  --foot:#0b77b3;
  --foot-line:#083f62;
  --btn:#2b2b2b;
}
*{box-sizing:border-box;margin:0;padding:0}
html,body{width:931px;height:1200px;overflow:hidden;background:var(--page);font-family:"Arimo",Arial,sans-serif;color:var(--ink)}
.page{position:relative;width:931px;height:1200px}
.abs{position:absolute}
.brand{left:78px;top:11px;display:flex;align-items:center;gap:8px}
.brand-dot{width:36px;height:36px;border-radius:50%;background:var(--orange)}
.brand-name{font-family:"Nunito",sans-serif;font-size:17px;font-weight:600;color:var(--orange);line-height:18px}
.brand-sub{font-size:8.5px;color:var(--grey);letter-spacing:.2px}
.contact-top{right:79px;top:19px;font-size:13px;text-decoration:underline;white-space:nowrap}
.swoosh{left:0;width:931px}
.sidenav{left:85px;top:84px;width:151px;height:726px;background:var(--nav)}
.sidenav ul{list-style:none;padding-top:9px}
.sidenav li{height:20.85px;line-height:20px;font-size:11.5px;padding-left:10px;border-bottom:1.5px solid #e6f1f6;white-space:nowrap}
.sidenav li.tool{background:var(--nav-dark)}
.main{left:246px;top:84px;width:600px;height:834px;background:var(--panel)}
.title{left:263px;top:100px;font-size:18px;color:var(--navy);font-weight:400;white-space:nowrap}
.continue{left:730px;top:105px;font-size:12px;text-decoration:underline;white-space:nowrap}
.photo-frame{left:260px;top:143px;width:319px;height:163px;border:1px solid #eef6fa;padding:4px}
.photo{width:100%;height:100%;background:linear-gradient(180deg,#dbe9cf 0%,#9bbf72 45%,#c9b08c 75%,#f4efe6 100%)}
.prices{left:260px;top:323px;width:319px;border-collapse:collapse;color:var(--link);font-size:14px}
.prices th{font-weight:400;height:22px;border:1px solid #eef6fa}
.prices td{height:24.7px;text-align:center;border-right:1px solid #eef6fa}
.prices td:last-child{border-right:none}
.actions{left:375px;top:526px;display:flex;flex-direction:column;gap:6px}
.btn{width:97px;height:18px;border-radius:9px;background:var(--btn);color:#fff;font-size:9px;font-weight:700;display:flex;align-items:center;justify-content:flex-end;gap:3px;padding-right:1px;white-space:nowrap;letter-spacing:-.1px}
.btn i{flex:none;width:16px;height:16px;border-radius:50%;background:#fff;border:2px solid #5fa7d6}
.info{left:603px;width:236px;font-size:12px;letter-spacing:-.2px}
.info h2,.info h3{font-size:12.5px;font-weight:700}
.note{font-size:8.5px;font-style:italic;line-height:15px}
.thumb-frame{left:602px;top:816px;width:236px;height:87px;border:1px solid #eef6fa;padding:4px}
.thumb-bg{width:100%;height:100%;background:#e2f1fa;display:flex;justify-content:center}
.thumb{width:155px;height:100%;background:linear-gradient(180deg,#e6efdc 0%,#9dbf78 50%,#bba583 80%,#f5f1ea 100%)}
.footer{left:0;top:945px;width:931px;height:255px;background:var(--foot)}
.rule{width:1px;top:959px;height:197px;background:var(--foot-line)}
.foot-h{font-family:"Nunito",sans-serif;font-size:18px;color:#111;font-weight:400}
.foot-list{list-style:none;font-family:"Roboto Condensed",sans-serif;font-size:14px;color:#0a1a2a;letter-spacing:-.3px;white-space:nowrap}
.foot-list li{height:19px;line-height:19px}
.search{left:676px;top:991px;width:138px;height:23px;background:#fff;border:1px solid #cfe3ef}
.go{left:823px;top:994px;font-family:"Roboto Condensed",sans-serif;font-size:14px}
.copy{left:0;width:931px;top:1165px;text-align:center;font-family:"Roboto Condensed",sans-serif;font-size:13px}
</style>
</head>
<body>
<div class="page">
  <header>
    <div class="abs brand">
      <span class="brand-dot"></span>
      <div><div class="brand-name">BrightWares</div><div class="brand-sub">DISTRIBUTOR WEBSITE SOLUTIONS</div></div>
    </div>
    <div class="abs contact-top">Sample Buyer . (555) 014-2287 . hello@brightwares.example</div>
    <svg class="abs swoosh" style="top:38px" width="931" height="34" viewBox="0 0 931 34">
      <path d="M0 26 C250 16 600 12 931 4 L931 12 C600 16 300 20 0 30 Z" fill="var(--orange)"/>
      <path d="M0 28 C300 22 620 20 931 12 L931 16 C620 24 300 28 0 32 Z" fill="var(--foot)"/>
    </svg>
  </header>

  <nav class="abs sidenav">
    <ul>
      <li>Your picks</li><li>Apparel</li><li>Auto</li><li>Award &amp; Recognition</li><li>Bags &amp; Totes</li>
      <li>Business Supplies</li><li>Calendars, Books &amp; Cards</li><li>Caps &amp; Hats</li><li>Clocks &amp; Watches</li>
      <li>Company Outings</li><li>Computer</li><li>Corporate Gifts</li><li>Desktop &amp; Office</li><li>Eco Friendly</li>
      <li>Electronics</li><li>Executive Gifts</li><li>Food, Candy &amp; Drink</li><li>Games &amp; Novelties</li>
      <li>Gift Sets</li><li>Golf, Sports &amp; Outdoors</li><li>Healthcare &amp; Safety</li><li>Holiday</li>
      <li>Home &amp; Housewares</li><li>Keychains</li><li>Mugs &amp; Drinkware</li><li>Notebooks &amp; Folios</li>
      <li>Pocket &amp; Purse</li><li>Stress Balls &amp; Relievers</li><li>Tools &amp; Hardware</li><li>Tradeshows &amp; Events</li>
      <li>Travel &amp; Luggage</li><li>Writing Instruments</li><li class="tool">Advanced Search</li><li class="tool">Recently Viewed Items</li>
    </ul>
  </nav>

  <main>
    <div class="abs main"></div>
    <h1 class="abs title">Leafwell Trio Planter Kit (LW# 418305)</h1>
    <a class="abs continue">Continue shopping</a>
    <div class="abs photo-frame"><div class="photo" role="img" aria-label="Three bamboo pots with herbs on a tray"></div></div>
    <table class="abs prices">
      <tr><th>Quantity</th><th>Price</th></tr>
      <tr><td>25</td><td>$12.86</td></tr>
      <tr><td>100</td><td>$12.43</td></tr>
      <tr><td>250</td><td>$12.00</td></tr>
      <tr><td>500</td><td>$11.57</td></tr>
      <tr><td>1000</td><td>$11.14</td></tr>
    </table>
    <div class="abs actions">
      <div class="btn">REQUEST INFO <i></i></div>
      <div class="btn">ORDER SAMPLE <i></i></div>
      <div class="btn">ADD TO CART <i></i></div>
    </div>

    <h2 class="abs info" style="top:140px;font-size:14px">Product Information</h2>
    <h3 class="abs info" style="top:172px">Leafwell Trio Planter Kit (LW# 418305)</h3>
    <p class="abs info" style="top:197px;line-height:24.5px">100% Biodegradable Bamboo.<br>Decomposition is a slow process in which the pot begins to age and small cracks become visible, Once the pot begins decomposition you may transfer your plant with the pot into the ground, This will prevent transplant shock.</p>
    <p class="abs info" style="top:351px;line-height:24.5px">Through its decomposition, organic properties from the bamboo provide nutrients to the soil, If used indoors, these bamboo pots will begin to decompose after 3 years, If kept outdoors they will begin to decompose after 2 years, If dropped into the trash, they completely degrade within 6 months.</p>
    <p class="abs info" style="top:538px">Size : 12 5/8" x 4 1/4" x 4 1/4"</p>
    <h3 class="abs info" style="top:568px">Price Includes</h3>
    <p class="abs info" style="top:592px">One Color/Location Imprint</p>
    <h3 class="abs info" style="top:622px">Production Time *</h3>
    <p class="abs info" style="top:648px">3 Working Days</p>
    <h3 class="abs info" style="top:678px">Setup Charge (per color)</h3>
    <p class="abs info" style="top:702px">$31.25</p>
    <h3 class="abs info" style="top:732px">Available Colors</h3>
    <p class="abs info" style="top:757px">Mocha Sandstone</p>
    <p class="abs info note" style="top:773px">* After credit, art and proof approval, excluding shipping time.</p>
    <div class="abs thumb-frame"><div class="thumb-bg"><div class="thumb" role="img" aria-label="Thumbnail of bamboo herb planter"></div></div></div>
  </main>

  <footer>
    <svg class="abs swoosh" style="top:922px" width="931" height="30" viewBox="0 0 931 30">
      <path d="M0 10 C300 2 620 6 931 14 L931 18 C620 10 300 8 0 16 Z" fill="var(--orange)"/>
      <path d="M0 18 C300 10 620 14 931 20 L931 30 L0 30 Z" fill="var(--foot)"/>
    </svg>
    <div class="abs footer"></div>
    <div class="abs rule" style="left:78px"></div>
    <div class="abs rule" style="left:475px"></div>
    <div class="abs rule" style="left:664px"></div>

    <h4 class="abs foot-h" style="left:92px;top:958px">Shop By Category</h4>
    <ul class="abs foot-list" style="left:90px;top:988px"><li>Apparel</li><li>Business Supplies</li><li>Company Outings</li><li>Eco Friendly</li><li>Food, Candy &amp; Drink</li><li>Golf, Sports &amp; Outdoors</li><li>Mugs &amp; Drinkware</li><li>Tradeshows &amp; Events</li></ul>
    <ul class="abs foot-list" style="left:227px;top:988px"><li>Awards &amp; Recognition</li><li>Caps &amp; Hats</li><li>Corporate Gifts</li><li>Electronics</li><li>Games &amp; Novelties</li><li>Healthcare &amp; Safety</li><li>Notebooks &amp; Folios</li><li>Writing Instruments</li></ul>
    <ul class="abs foot-list" style="left:352px;top:988px"><li>Bags &amp; Totes</li><li>Clocks &amp; Watches</li><li>Desktop &amp; Office</li><li>Executive Gifts</li><li>Gift Sets</li><li>Keychains</li><li>Tools &amp; Hardware</li></ul>

    <h4 class="abs foot-h" style="left:486px;top:957px">Shop By Price</h4>
    <ul class="abs foot-list" style="left:525px;top:988px"><li>Under $5</li><li>$5 - $10</li><li>$10 - $20</li><li>$20 - $50</li><li>$50 - $100</li><li>$100 - $200</li><li>Over $200</li></ul>

    <h4 class="abs foot-h" style="left:676px;top:957px">Quick Search</h4>
    <div class="abs search"></div>
    <span class="abs go">Go</span>
    <h4 class="abs foot-h" style="left:676px;top:1032px">Contact Us</h4>
    <ul class="abs foot-list" style="left:676px;top:1062px"><li style="height:15px;line-height:15px">hello@brightwares.example</li><li style="height:15px;line-height:15px">www.brightwares.example</li></ul>

    <p class="abs copy">Copyright © 2010 . BrightWares.example V3 . All Rights Reserved.</p>
  </footer>
</div>
</body>
</html>
```